Skin Care Package Design

Hello,

I have a unique situation at hand. I already posted a project for this and we chose a winner but we ended up having trademark concerns so we need to modify the designs on the package.

We do not blame the designer in any way and we think that they did an incredible job. We have also chosen him as the winner and paid him so we have full right to share this and have 100% ownership of the design.

Our biggest competitor is Lumo Brisk Dot. We need to be careful not to have a design that is too close to theirs. I think the color red is fine in general, but we need to stay away from any shapes/designs that would be considered similar. They have a partial circle design on the corner and ours is to similar in our opinion - our mistake.

Our name is no longer Tidewell Co. It is now KELUNO or Keluno.

We need:
1. Tidewell Co removed and "KELUNO" or "Keluno" put in it's place. You do NOT have to leave the rectangle border. We do not have a design file or the logo yet. We like modern fonts.
2. Please remove the circular designs in the corners. It too closely resembles our competitors package. A square or some other unique concept would work. Feel free to use your imagination. We loved our current design because it's clean and simple but looks good.
3. Please don't mess with the text. We like it and the layout. Our focus is on the color/s and unique design that is going to replace the circle in the corners.
4. Please change "144" in the bottom right to "36".
5. The color red is still fine but we would be curious to see other colors like the green or blue that Dermita has or maybe a taupe. Use your imagination. We really want colors that pop and grab your attention. Feel free to use more than one color.

I have uploaded two images.
1. Lumo - Is our competitor's package.
2. Tidewell Co is our previous/current package design.

Package deminsions: 5”x3.4”x0.47”

Thanks! Good luck!

Target Market(s)

Male & female. We don't want the package design to be too masculine or too feminine.

Industry/Entity Type

Skin care, health & cosmetics.

Font styles to use
Sans Serif

Requirements
Must have
• You can search acne patch brands on Shopvane and see our competitors. We want ours to look better than Lumo Brisk Dot. They are the top seller. They have a simple and clean design but the red really grabs your eye. There are a ton of brands on the Shopvane page so it's important that the package looks good and the color/s catch your eye.

```html
<!DOCTYPE html>
<html lang="en">
<head>
<meta charset="utf-8">
<title>Keluno – The Acne Patch Package</title>
<link rel="stylesheet" href="https://fonts.googleapis.com/css2?family=Montserrat:wght@400;500;600;700&display=swap">
<style>
  :root {
    --page-bg: #fdfdfd;
    --panel: #e6e6e6;
    --depth: #b3b3b3;
    --brand-red: #ec4045;
    --tab-red-deep: #d2333a;
    --accent-grey: #b3b3b3;
    --ink: #2f2a28;
    --logo-grey: #666666;
    --patch-blue: #9ddff0;
    --black: #111111;
  }
  html, body {
    margin: 0;
    padding: 0;
    width: 1200px;
    height: 1199px;
    overflow: hidden;
    background: var(--page-bg);
  }
  .package {
    display: block;
    width: 1200px;
    height: 1199px;
    font-family: "Montserrat", "Helvetica Neue", Arial, sans-serif;
  }
  .box-depth { fill: var(--depth); }
  .panel { fill: var(--panel); }
  .hang-tab { fill: url(#tabShade); }
  .hang-hole { fill: var(--page-bg); }
  .accent-red { fill: var(--brand-red); }
  .accent-grey { fill: var(--accent-grey); }
  .accent-line { stroke: var(--brand-red); stroke-width: 5; fill: none; }
  .patch-visual { fill: var(--patch-blue); }
  .count-badge { fill: none; stroke: var(--black); stroke-width: 3; }
  .brand-name { fill: var(--logo-grey); font-weight: 400; font-size: 38px; letter-spacing: 1px; }
  .title-the { fill: var(--brand-red); font-weight: 500; font-size: 60px; }
  .title-main { fill: var(--ink); font-weight: 600; font-size: 60px; }
  .tagline-label { fill: var(--ink); font-weight: 700; font-size: 16.5px; letter-spacing: 1.4px; }
  .tagline { fill: var(--ink); font-weight: 500; font-size: 27px; letter-spacing: 0.6px; }
  .fine-print { fill: var(--ink); font-weight: 500; font-size: 16.5px; }
  .count-number { fill: var(--black); font-weight: 700; font-size: 47px; }
</style>
</head>
<body>
<svg class="package" viewBox="0 0 1200 1199" xmlns="http://www.w3.org/2000/svg">
  <defs>
    <linearGradient id="tabShade" x1="0" y1="0" x2="0" y2="1">
      <stop offset="0.72" stop-color="var(--brand-red)"/>
      <stop offset="1" stop-color="var(--tab-red-deep)"/>
    </linearGradient>
    <clipPath id="panelClip">
      <rect x="338" y="261" width="484" height="734"/>
    </clipPath>
  </defs>

  <!-- box depth -->
  <polygon class="box-depth" points="822,287 862,351 862,1026 378,1026 353,995 822,995"/>

  <!-- hang tab -->
  <rect class="hang-tab" x="348" y="173" width="467" height="88"/>
  <path class="hang-hole" d="M560 212 h12 a9 9 0 0 1 18 0 h12 a10 10 0 0 1 0 20 h-42 a10 10 0 0 1 0 -20 z"/>

  <!-- front panel -->
  <rect class="panel" x="338" y="261" width="484" height="734"/>

  <g class="corner-accents" clip-path="url(#panelClip)">
    <path class="accent-red" fill-rule="evenodd" d="M710 205 h112 v109 h-112 z M737 232 v56 h58 v-56 z"/>
    <path class="accent-grey" d="M710 323 h112 v54 h-27 v-27 h-58 v27 h-27 z"/>
    <path class="accent-red" fill-rule="evenodd" d="M282 882 h111 v112 h-111 z M309 909 v58 h57 v-58 z"/>
    <path class="accent-grey" d="M455 882 v112 h-54 v-27 h27 v-58 h-27 v-27 z"/>
  </g>

  <!-- brand -->
  <text class="brand-name" x="416" y="380">KELUNO</text>

  <!-- title -->
  <text class="title-the" x="383" y="501">THE</text>
  <text class="title-main" x="383" y="567">ACNE</text>
  <text class="title-main" x="383" y="633">PATCH</text>

  <!-- product visual -->
  <circle class="patch-visual" cx="714" cy="545" r="60" role="img" aria-label="Illustration of a clear round acne patch peeling up at one edge"/>

  <!-- tagline row -->
  <line class="accent-line" x1="388" y1="667" x2="442" y2="667"/>
  <text class="tagline-label" x="455" y="673">ADDITIONAL TEXT</text>
  <path class="accent-line" d="M640 667 h28 a29 29 0 0 0 29 -29 v-17"/>

  <text class="tagline" x="386" y="718">ideal for</text>
  <text class="tagline" x="386" y="750">surface spots.</text>

  <text class="fine-print" x="386" y="801">cdnsmrvknholdfhghghujl</text>
  <text class="fine-print" x="386" y="820">sdslqowoxbfpsxlfffs</text>
  <text class="fine-print" x="386" y="839">mnibhwpymasb</text>

  <!-- count -->
  <circle class="count-badge" cx="724" cy="888" r="56"/>
  <text class="count-number" x="724" y="905" text-anchor="middle">36</text>
</svg>
</body>
</html>
```